redesign my website bluekelpvoyages.com and make it user friendly

I already have a website, bluekelpvoyages.com, and want a redesign in WordPress with Elementor Pro, using the same text/content. The goal is to improve:

Design quality (colors, fonts, spacing, visual flow)
User experience (easy navigation, clear offers)
Conversion readiness (calls-to-action, trust signals, booking flow)
Technical side (SEO basics, fast speed, full mobile responsiveness)

The site should look modern, clean, fun, engaging, interactive and optimized for speed and usability.

I would like the 11 page to be consolidate dto 6 as follows: Home (main landing, highlights)

Sailboat Trips (all packages, itineraries, pricing)
Boats (fleet details, features, photos)
How It Works (booking process, FAQs, travel info, what to expect)
Blog
Contact Us (form, WhatsApp, phone, etc.)

Target Market(s)

sailboat trip customers for Coral Mira Keys in Panama

Industry/Entity Type

Travel, Boat Tour Agency

Coding

Number of Pages Required

3 page

Font styles to use
Sans Serif
Other font styles liked:
• Oswalg and sans serif

Colors
0054AA
0677BA
7BADD7
CADEEF
E8F1F8
0094D4
00A9DD
6FCCEA
C7EBF8
E9F6FB
FFC000
F8CF3A
FAE287
FDF2CF
FEFAEE
F0912C
F2A743
F7CA91
FBE8D2
FDF5EE

Requirements
Must have
• Home (main landing, highlights) Sailboat Trips (all packages, itineraries, pricing) Boats (fleet details, features, photos) How It Works (booking process, FAQs, travel info, what to expect) Blog (updates, travel tips, inspiration) Contact Us (form, WhatsApp, phone, etc.)
Nice to have
• I want it to look professionla and be very user friendy to entice people to contact me to book boat trips
Should not have
• a store

```html
<!DOCTYPE html>
<html lang="en">
<head>
<meta charset="utf-8">
<title>Blue Kelp Voyages – Coral Mira Keys Sailing Tours</title>
<link href="https://fonts.googleapis.com/css2?family=League+Gothic&family=Oswald:wght@400;500;600&family=Poppins:wght@400;500;600&display=swap" rel="stylesheet">
<style>
:root{
  --blue-deep:#0054AA;
  --blue:#0677BA;
  --blue-mid:#0094D4;
  --sky:#00A9DD;
  --sky-light:#6FCCEA;
  --ice:#E9F6FB;
  --yellow:#FFC000;
  --yellow-soft:#F8CF3A;
  --orange:#F0912C;
  --orange-light:#F2A743;
  --ink:#1d2733;
  --muted:#5b6470;
  --white:#ffffff;
  --head:"League Gothic", "Oswald", sans-serif;
  --ui:"Oswald", sans-serif;
  --body:"Poppins", sans-serif;
}
*{box-sizing:border-box;margin:0;padding:0}
html,body{width:1200px;height:4928px;overflow:hidden;background:var(--white)}
body{font-family:var(--body);color:var(--ink)}
.page{position:relative;width:1200px;height:4928px;overflow:hidden}
.abs{position:absolute}
.btn{position:absolute;display:flex;align-items:center;justify-content:center;border-radius:20px;font-family:var(--ui);font-size:14px;letter-spacing:.5px;color:var(--white);text-transform:uppercase;background:linear-gradient(180deg,var(--orange-light),var(--orange));box-shadow:0 4px 10px rgba(240,145,44,.35)}
.btn--blue{background:linear-gradient(180deg,var(--blue-mid),var(--blue-deep));box-shadow:0 4px 10px rgba(0,84,170,.35)}
.heading{font-family:var(--head);color:var(--yellow);text-transform:uppercase;font-weight:400;line-height:1;letter-spacing:1px}

/* hero */
.hero{left:0;top:0;width:1200px;height:823px;background:linear-gradient(180deg,#2f6fc2 0%,#6ea6dc 28%,#cfe4f4 44%,#3fa6c9 56%,#17c2d6 72%,#0aa3c8 100%)}
.nav{left:150px;top:32px;width:900px;height:56px;border-radius:28px;background:var(--white);box-shadow:0 6px 18px rgba(0,0,0,.12)}
.nav a{position:absolute;top:19px;font-family:var(--ui);font-size:14px;color:#8a93a0;text-decoration:none;text-transform:uppercase}
.nav a.active{color:var(--blue-deep);font-weight:600}
.logo-badge{left:545px;top:10px;width:110px;height:110px;border-radius:50%;background:var(--white);box-shadow:0 4px 14px rgba(0,0,0,.15);display:flex;flex-direction:column;align-items:center;justify-content:center;gap:6px}
.logo-badge .dot{width:16px;height:16px;border-radius:50%;background:var(--yellow)}
.logo-badge span{font-family:var(--ui);font-size:12px;font-weight:500;color:var(--blue-deep);text-transform:uppercase;text-align:center;line-height:1.2}
.hero-title{left:150px;top:185px;font-size:200px;color:var(--yellow)}
.hero-sub{left:150px;top:392px;font-size:118px;color:var(--white)}
.hero-tag{left:396px;top:410px;font-family:var(--head);font-size:42px;line-height:1.05;color:var(--white);text-transform:uppercase}
.yacht-hero{left:520px;top:40px;width:560px;height:680px;border-radius:40% 40% 20% 20%/60% 60% 10% 10%;background:linear-gradient(180deg,rgba(255,255,255,.85),rgba(225,235,245,.7) 70%,rgba(255,255,255,.9))}

/* discover card */
.discover{left:150px;top:693px;width:900px;height:448px;background:var(--white);border-radius:12px;box-shadow:0 10px 30px rgba(0,60,120,.1)}
.discover .heading{position:absolute;left:0;width:900px;top:22px;text-align:center;font-size:64px}
.service{position:absolute;top:130px;width:240px}
.service h3{font-family:var(--head);font-size:32px;font-weight:400;color:var(--blue-deep);text-transform:uppercase;letter-spacing:1px;margin:14px 0 10px}
.service p{font-size:11px;line-height:1.8;color:var(--muted)}

/* popular */
.yacht-side{left:57px;top:1282px;width:300px;height:210px;border-radius:50% 10px 10px 50%/60% 10px 10px 40%;background:linear-gradient(180deg,#f4f7fa,#dfe7ee 60%,#bcd8ea)}
.trip-card{left:345px;top:1244px;width:287px;height:316px;background:var(--white);border-radius:14px;box-shadow:0 10px 30px rgba(0,0,0,.12)}
.trip-photo{position:absolute;left:9px;top:10px;width:269px;height:134px;border-radius:10px;background:linear-gradient(180deg,#7cc0ec 0%,#b9dcef 45%,#2fb4c9 70%,#e9dcb8 100%)}
.ongoing{left:211px;top:1547px;width:210px;height:99px;background:var(--white);border-radius:12px;box-shadow:0 10px 30px rgba(0,0,0,.12)}
.popular-title{left:664px;top:1230px;font-size:84px;line-height:.95}
.popular-text{left:664px;top:1414px;width:390px;font-size:11px;line-height:1.8;color:var(--muted)}
.ticks{left:664px;top:1508px;width:400px;list-style:none}
.ticks li{position:relative;padding-left:20px;font-size:11px;font-weight:500;line-height:1.7;margin-bottom:6px}
.ticks li::before{content:"";position:absolute;left:0;top:4px;width:12px;height:12px;border-radius:50%;background:var(--yellow)}

/* fleet */
.fleet{left:0;top:1748px;width:1200px;height:859px;background:radial-gradient(ellipse at 50% 40%,#1e80d6 0%,#0b5fbc 55%,#0a4ea0 100%)}
.fleet-photo{position:absolute;background:linear-gradient(180deg,#d7e7f5 0%,#f6f8fb 40%,#9cc2e3 70%,#3b7db8 100%)}
.arrow{position:absolute;width:38px;height:38px;border-radius:50%;background:var(--orange);display:flex;align-items:center;justify-content:center}

/* how */
.how-photo{left:193px;top:2829px;width:427px;height:438px;border-radius:6px;background:linear-gradient(180deg,#5ea1de 0%,#d8e6f2 35%,#f1f4f7 55%,#2a6aa8 75%,#0d4a8a 100%)}
.how-card{left:566px;top:2896px;width:441px;height:304px;background:var(--white);border-radius:8px;box-shadow:0 10px 30px rgba(0,0,0,.12)}
.step{position:absolute;left:38px;width:370px}
.step h3{position:absolute;left:58px;top:0;font-family:var(--head);font-weight:400;font-size:32px;color:var(--blue-deep);letter-spacing:1px;text-transform:uppercase}
.step p{position:absolute;left:58px;top:36px;width:320px;font-size:8.5px;line-height:1.8;color:var(--muted)}

/* ready */
.ready{left:150px;top:3407px;width:900px;height:249px;border-radius:10px;background:linear-gradient(90deg,#0a5ab2 0%,#0677BA 55%,#6ea8d8 100%)}
.ready-boat{left:500px;top:3372px;width:700px;height:310px;border-radius:60% 10% 30% 40%/70% 20% 40% 40%;background:linear-gradient(180deg,#fbfcfd 0%,#e3e9ef 55%,#a9b9c8 100%)}

/* testimonials */
.avatar{position:absolute;border-radius:50%;border:4px solid var(--white);box-shadow:0 4px 12px rgba(0,0,0,.15)}

/* footer */
.footer{left:0;top:4320px;width:1200px;height:608px;background:radial-gradient(ellipse at 40% 30%,#1d79d0 0%,#0b5cb6 60%,#094a9c 100%);color:var(--white)}
.foot-col{position:absolute;top:250px}
.foot-col h4{font-family:var(--ui);font-weight:500;font-size:14px;text-transform:uppercase;margin-bottom:16px}
.foot-col li{list-style:none;font-size:11px;line-height:27px;opacity:.9}
.social{position:absolute;top:480px;width:30px;height:30px;border-radius:50%;background:var(--orange)}
</style>
</head>
<body>
<div class="page">

  <!-- HERO -->
  <section class="abs hero" role="img" aria-label="Catamaran under white sails on turquoise water beside a palm island under a blue sky"></section>
  <div class="abs yacht-hero" role="img" aria-label="White sailing catamaran with tall sails"></div>

  <nav class="abs nav">
    <a class="active" style="left:36px">Home</a>
    <a style="left:94px">Sailboat Trips</a>
    <a style="left:214px">Boats</a>
    <a style="left:276px">How It Works</a>
    <a style="left:536px">Blog</a>
    <a style="left:590px">Contact Us</a>
    <span class="btn" style="left:728px;top:12px;width:134px;height:32px">Get Started</span>
  </nav>
  <div class="abs logo-badge"><div class="dot"></div><span>Blue Kelp<br>Voyages</span></div>

  <h1 class="abs heading hero-title">Coral Mira</h1>
  <div class="abs heading hero-sub">Keys</div>
  <div class="abs hero-tag" style="left:330px">Ultimate Beaches &amp;<br>Catamaran Tours</div>
  <span class="btn" style="left:150px;top:565px;width:196px;height:35px">Charter Inquiry Form</span>

  <!-- DISCOVER -->
  <section class="abs discover">
    <h2 class="heading">Discover Ultimate Panama Sailing Tours</h2>
    <div class="service" style="left:76px">
      <svg width="30" height="34" viewBox="0 0 30 34" fill="none" stroke="#1d2733" stroke-width="1.8"><circle cx="15" cy="5" r="3"/><path d="M15 8v24M8 13h14M3 20c1 7 6 11 12 12 6-1 11-5 12-12"/></svg>
      <h3>Private Charters</h3>
      <p>Sail The Beautiful Islands And Beaches Of Coral Mira On A Private All-Inclusive Catamaran. Enjoy A Custom Itinerary, Friendly Crew, And Flexible Options To Fit Any Budget—Perfect For A Relaxing Escape.</p>
    </div>
    <div class="service" style="left:336px">
      <svg width="34" height="34" viewBox="0 0 34 34" fill="none" stroke="#1d2733" stroke-width="1.8"><circle cx="17" cy="9" r="5"/><circle cx="7" cy="20" r="4"/><circle cx="27" cy="20" r="4"/><path d="M2 32c0-4 2-6 5-6s5 2 5 6M22 32c0-4 2-6 5-6s5 2 5 6M11 24c1-4 3-6 6-6s5 2 6 6"/></svg>
      <h3>Shared Charters</h3>
      <p>Share The Experience With Others For A More Affordable Alternative To A Private Charter. Perfect For Couples, Solo Travelers, And Small Groups—Enjoy Coral Mira Beaches, Clear Waters, Great Meals, And A Relaxed Atmosphere With A Welcoming Crew.</p>
    </div>
    <div class="service" style="left:595px">
      <svg width="38" height="34" viewBox="0 0 38 34" fill="none" stroke="#1d2733" stroke-width="1.8"><path d="M19 3v20M19 5l10 16H19M19 8l-8 13h8M3 24h32l-4 6H7z"/><path d="M2 33c4-2 6-2 9 0s6 2 9 0 6-2 9 0 5 2 8 0"/></svg>
      <h3>Family Friendly Boat Trips</h3>
      <p>Coral Mira Is Perfect For Kids, With Calm Waters, Safe Snorkeling, And Fun Island-Hopping. Families Love The Mix Of Adventure And Culture—An Ideal Way To Explore Panama Together.</p>
    </div>
    <span class="btn" style="left:370px;top:382px;width:160px;height:36px">Request A Quote</span>
  </section>

  <!-- POPULAR TRIPS -->
  <div class="abs yacht-side" role="img" aria-label="White motor yacht cruising with spray"></div>
  <div class="abs trip-card">
    <div class="trip-photo" role="img" aria-label="Beach resort towers along turquoise shoreline"></div>
    <div class="abs" style="left:16px;top:158px;font-size:13px">Trip to Hawaii</div>
    <div class="abs" style="left:16px;top:182px;font-size:9px;color:var(--muted)">14-29 June &nbsp;|&nbsp; by R. Calloway</div>
    <div class="abs" style="left:16px;top:210px;width:24px;height:24px;border-radius:50%;background:#FDF2CF"></div>
    <div class="abs" style="left:50px;top:210px;width:24px;height:24px;border-radius:50%;background:#FDF2CF"></div>
    <div class="abs" style="left:84px;top:210px;width:24px;height:24px;border-radius:50%;background:var(--ice)"></div>
    <div class="abs" style="left:16px;top:264px;font-size:9px;color:var(--muted)"><span style="display:inline-block;width:10px;height:10px;background:var(--sky-light);margin-right:8px;vertical-align:middle"></span>60 people are interested</div>
    <svg class="abs" style="left:252px;top:262px" width="18" height="16" viewBox="0 0 18 16" fill="none" stroke="#F0912C" stroke-width="1.5"><path d="M9 15S1 10 1 5a4 4 0 0 1 8-1 4 4 0 0 1 8 1c0 5-8 10-8 10z"/></svg>
  </div>
  <div class="abs ongoing">
    <div class="abs" style="left:16px;top:22px;width:38px;height:38px;border-radius:50%;background:#8a5a4a" role="img" aria-label="Trip thumbnail"></div>
    <div class="abs" style="left:66px;top:18px;font-size:9px;color:var(--muted)">Ongoing</div>
    <div class="abs" style="left:66px;top:34px;font-size:12px">Trip to rome</div>
    <div class="abs" style="left:66px;top:60px;font-size:9px;color:var(--blue-deep)">40% completed</div>
    <div class="abs" style="left:66px;top:78px;width:124px;height:4px;border-radius:2px;background:var(--ice)"></div>
    <div class="abs" style="left:66px;top:78px;width:50px;height:4px;border-radius:2px;background:var(--blue-deep)"></div>
  </div>
  <h2 class="abs heading popular-title">Our &nbsp;Most<br>Popular &nbsp;Trips</h2>
  <p class="abs popular-text">Lorem Ipsum Dolor Sit Amet Consectetur. Eget Adipiscing Odio Malesuada Mauris Amet. Faucibus Nullam Amet Arcu Neque Ac Nec. Odio Turpis Dui Enim Hac Varius Eu. Aliquet Dolor Lectus Volutpat Egestas Donec Amet Fermentum Et Turpis.</p>
  <ul class="abs ticks">
    <li>Lorem Ipsum Dolor Sit Amet Consectetur. Eget Adipiscing Odio Malesuada</li>
    <li>Lorem Ipsum Dolor Sit Amet Consectetur. Dolor Nunc Nunc Ullamcorper.</li>
    <li>Dolor Sit Amet Consectetur. Eget Adipiscing Odio Malesuada</li>
  </ul>
  <span class="btn" style="left:664px;top:1617px;width:144px;height:37px">Explore More</span>
  <span class="btn btn--blue" style="left:834px;top:1617px;width:211px;height:37px">Book Your Trip With Us</span>

  <!-- FLEET -->
  <section class="abs fleet" role="img" aria-label="Deep blue ocean water texture background"></section>
  <h2 class="abs heading" style="left:0;width:1200px;top:1796px;text-align:center;font-size:84px">Our Fleet, Your Adventure</h2>
  <div class="fleet-photo" style="left:150px;top:1956px;width:190px;height:284px" role="img" aria-label="Sailboat heeling under full sail"></div>
  <div class="fleet-photo" style="left:865px;top:1956px;width:185px;height:284px" role="img" aria-label="Sailing yacht on open sea"></div>
  <div class="fleet-photo" style="left:338px;top:1927px;width:524px;height:339px;border:4px solid var(--white);border-radius:8px" role="img" aria-label="Large white sailing yacht at sea"></div>
  <h3 class="abs" style="left:0;width:1200px;top:2296px;text-align:center;font-family:var(--head);font-weight:400;font-size:44px;color:var(--white);letter-spacing:2px">BOAT &nbsp;NAME</h3>
  <p class="abs" style="left:380px;width:440px;top:2352px;text-align:center;font-size:10px;line-height:2.2;color:var(--white)">Lorem Ipsum Dolor Sit Amet Consectetur. Faucibus Diam Sodales A Commodo Massa Nisl. Feugiat Bibendum Lacus Ut Dolor Dictum Amet Dictum Nisi. Risus Eu Molestie Urna Vitae Rutrum Nec Eu. Magna Leo Sed Eu Ut Nisi Arcu.</p>
  <div class="abs" style="left:0;width:1200px;top:2428px;text-align:center;font-size:13px;color:var(--white)"><span style="color:var(--yellow)">⌂</span>&nbsp; 2 Cabins &nbsp;&nbsp;<span style="color:var(--yellow)">⚓</span>&nbsp; Marlowe &nbsp;&nbsp;<span style="color:var(--yellow)">⛽</span>&nbsp; petrol</div>
  <div class="abs" style="left:0;width:1200px;top:2462px;text-align:center;font-family:var(--ui);font-size:13px;color:var(--white)">READ MORE +</div>
  <span class="btn" style="left:150px;top:2517px;width:195px;height:35px">Explore Our All Boat</span>
  <div class="arrow" style="left:965px;top:2515px"><svg width="12" height="12" viewBox="0 0 12 12" fill="none" stroke="#fff" stroke-width="2"><path d="M8 2L4 6l4 4"/></svg></div>
  <div class="arrow" style="left:1011px;top:2515px"><svg width="12" height="12" viewBox="0 0 12 12" fill="none" stroke="#fff" stroke-width="2"><path d="M4 2l4 4-4 4"/></svg></div>

  <!-- HOW IT WORKS -->
  <h2 class="abs heading" style="left:0;width:1200px;top:2696px;text-align:center;font-size:84px">How It Works</h2>
  <div class="abs how-photo" role="img" aria-label="Sailboat heeling through waves under a blue sky"></div>
  <div class="abs how-card">
    <div class="step" style="top:46px">
      <svg class="abs" style="left:0;top:6px" width="42" height="42" viewBox="0 0 42 42" fill="none" stroke="#1d2733" stroke-width="1.6"><circle cx="21" cy="21" r="16"/><path d="M5 21h32M21 5c6 6 6 26 0 32M21 5c-6 6-6 26 0 32"/></svg>
      <h3>Choose &nbsp;Destination</h3>
      <p>Lorem Ipsum Dolor Sit Amet Consectetur. Odio Morbi Non Faucibus Phasellus Curabitur Viverra Eu Amet Vel.</p>
    </div>
    <div class="step" style="top:130px">
      <svg class="abs" style="left:0;top:6px" width="42" height="42" viewBox="0 0 42 42" fill="none" stroke="#1d2733" stroke-width="1.6"><rect x="4" y="8" width="30" height="26" rx="2"/><path d="M4 15h30M11 4v7M27 4v7"/><circle cx="32" cy="32" r="7" fill="#fff"/><path d="M32 28v4l3 2"/></svg>
      <h3>Check &nbsp;Availability</h3>
      <p>Lorem Ipsum Dolor Sit Amet Consectetur. Odio Morbi Non Faucibus Phasellus Curabitur Viverra Eu Amet Vel.</p>
    </div>
    <div class="step" style="top:214px">
      <svg class="abs" style="left:0;top:6px" width="42" height="42" viewBox="0 0 42 42" fill="none" stroke="#1d2733" stroke-width="1.8"><circle cx="24" cy="6" r="3"/><path d="M22 11l-6 10 8 4-4 12M22 11l8 6 6-2M16 21l-8 2"/></svg>
      <h3>Let's &nbsp;Go &nbsp;The &nbsp;Trip</h3>
      <p>Lorem Ipsum Dolor Sit Amet Consectetur. Odio Morbi Non Faucibus Phasellus Curabitur Viverra Eu Amet Vel.</p>
    </div>
  </div>

  <!-- READY TO SAIL -->
  <section class="abs ready"></section>
  <div class="abs ready-boat" role="img" aria-label="White luxury motor yacht"></div>
  <h2 class="abs heading" style="left:193px;top:3422px;font-size:84px">Ready To Sail?</h2>
  <p class="abs" style="left:193px;top:3516px;width:300px;font-size:10px;line-height:2.4;color:var(--white)">Your Paradise Escape Is Just One Click Away. Book Today And Let Us Take Care Of The Rest.</p>
  <span class="btn" style="left:193px;top:3593px;width:213px;height:35px">Book Your Sailboat Trip</span>

  <!-- TESTIMONIALS -->
  <h2 class="abs heading" style="left:0;width:1200px;top:3767px;text-align:center;font-size:84px;letter-spacing:3px">What &nbsp;Our &nbsp;Guests &nbsp;Say</h2>
  <svg class="abs" style="left:0;top:3880px" width="1200" height="220" viewBox="0 0 1200 220" fill="none">
    <path d="M0 150 C120 170 150 40 250 60 S380 200 470 90 S600 60 650 120 S760 60 840 40 S960 180 1040 120 S1150 90 1200 110" stroke="var(--blue)" stroke-width="1.5" stroke-dasharray="4 5"/>
    <circle cx="250" cy="124" r="5" fill="var(--blue-deep)"/>
    <circle cx="402" cy="100" r="4" fill="var(--blue-deep)"/>
    <circle cx="680" cy="98" r="5" fill="var(--blue-deep)"/>
    <circle cx="832" cy="162" r="4" fill="var(--blue-deep)"/>
    <circle cx="963" cy="46" r="4" fill="var(--blue-deep)"/>
    <circle cx="1090" cy="110" r="5" fill="var(--blue-deep)"/>
  </svg>
  <div class="avatar" style="left:164px;top:3921px;width:66px;height:66px;background:#f3c7c9" role="img" aria-label="Guest portrait"></div>
  <div class="avatar" style="left:287px;top:3964px;width:100px;height:100px;background:#b45fa3" role="img" aria-label="Guest portrait"></div>
  <div class="avatar" style="left:436px;top:3916px;width:66px;height:66px;background:#e8a9b0" role="img" aria-label="Guest portrait"></div>
  <div class="avatar" style="left:555px;top:3939px;width:84px;height:84px;background:#f5d3c8;border-color:var(--orange-light)" role="img" aria-label="Guest portrait"></div>
  <div class="avatar" style="left:708px;top:3912px;width:100px;height:100px;background:#c9a98a" role="img" aria-label="Guest portrait"></div>
  <div class="avatar" style="left:852px;top:3993px;width:76px;height:76px;background:#d8484d" role="img" aria-label="Guest portrait"></div>
  <div class="avatar" style="left:972px;top:3920px;width:84px;height:84px;background:#f09a3a" role="img" aria-label="Guest portrait"></div>
  <div class="abs" style="left:0;width:1200px;top:4110px;text-align:center;font-family:var(--ui);font-size:34px;color:var(--orange)">❝</div>
  <p class="abs" style="left:365px;width:470px;top:4152px;text-align:center;font-size:11px;font-style:italic;line-height:2.1;color:var(--ink)">Lorem Ipsum Dolor Sit Amet Consectetur. Dolor Dictum Nunc Quis Cras. Eget Aliquam Ac Odio Morbi Malesuada Cras Volutpat Urna Eget. Gravida Proin Odio Sit Amet Massa Pellentesque Sit. Condimentum Dictum Cras At Egestas Varius Eget. Vitae A Elit Et Dapibus Tellus Mattis Diam Orci Fermentum.</p>
  <div class="arrow" style="left:251px;top:4176px;width:32px;height:32px"><svg width="10" height="10" viewBox="0 0 12 12" fill="none" stroke="#fff" stroke-width="2"><path d="M8 2L4 6l4 4"/></svg></div>
  <div class="arrow" style="left:912px;top:4176px;width:32px;height:32px"><svg width="10" height="10" viewBox="0 0 12 12" fill="none" stroke="#fff" stroke-width="2"><path d="M4 2l4 4-4 4"/></svg></div>

  <!-- FOOTER -->
  <footer class="abs footer">
    <h2 class="abs heading" style="left:150px;top:60px;font-size:88px;letter-spacing:3px">Join &nbsp;The &nbsp;Crew</h2>
    <div class="abs" style="left:607px;top:76px;width:443px;height:48px;border-radius:24px;background:var(--white)">
      <span class="abs" style="left:20px;top:15px;font-family:var(--ui);font-size:13px;color:#7a8490">ENTER YOUR EMAIL</span>
      <span class="btn" style="left:260px;top:7px;width:168px;height:34px">Subscribe It Now</span>
    </div>
    <div class="abs" style="left:150px;top:207px;width:900px;height:1px;background:rgba(255,255,255,.35)"></div>
    <div class="abs" style="left:153px;top:272px;display:flex;align-items:center;gap:12px">
      <span style="width:30px;height:30px;border-radius:50%;background:var(--yellow)"></span>
      <span style="font-family:var(--ui);font-size:24px;font-weight:500;color:var(--white);text-transform:uppercase;line-height:1">Blue Kelp Voyages</span>
    </div>
    <div class="foot-col" style="left:534px"><h4>Used Full Links</h4><ul><li>Home</li><li>Sailboat Trips</li><li>Boats</li><li>How It Works</li><li>Blog</li><li>Contact Us</li></ul></div>
    <div class="foot-col" style="left:706px"><h4>Trip Location</h4><ul><li>Florida</li><li>Canada</li><li>UAE</li><li>United Kingdom</li></ul></div>
    <div class="foot-col" style="left:856px"><h4>Contact Info</h4>
      <ul>
        <li><svg width="12" height="12" viewBox="0 0 12 12" fill="none" stroke="#fff" stroke-width="1.2" style="vertical-align:middle;margin-right:10px"><path d="M6 11s4-4 4-6.5a4 4 0 0 0-8 0C2 7 6 11 6 11z"/><circle cx="6" cy="4.5" r="1.3"/></svg>14 Harbor Lane, Portobelo</li>
        <li><svg width="12" height="12" viewBox="0 0 12 12" fill="none" stroke="#fff" stroke-width="1.2" style="vertical-align:middle;margin-right:10px"><path d="M2 1h2.5l1 3-1.5 1a7 7 0 0 0 3 3l1-1.5 3 1V10a1 1 0 0 1-1 1A9 9 0 0 1 1 2a1 1 0 0 1 1-1z"/></svg>(507) 555-0148</li>
        <li><svg width="12" height="12" viewBox="0 0 12 12" fill="none" stroke="#fff" stroke-width="1.2" style="vertical-align:middle;margin-right:10px"><rect x="1" y="2.5" width="10" height="7" rx="1"/><path d="M1 3l5 4 5-4"/></svg>hello@bluekelpvoyages.com</li>
      </ul>
    </div>
    <span class="social" style="left:151px"></span>
    <span class="social" style="left:190px"></span>
    <span class="social" style="left:230px"></span>
    <div class="abs" style="left:150px;top:550px;width:900px;height:1px;background:rgba(255,255,255,.35)"></div>
    <div class="abs" style="left:150px;top:568px;font-size:9px;opacity:.9">Copyright © 2025 · All Rights Reserved</div>
    <div class="abs" style="left:900px;top:568px;font-size:9px;opacity:.9">Terms Of Use</div>
    <div class="abs" style="left:995px;top:568px;font-size:9px;opacity:.9">Terms Of Use</div>
  </footer>

</div>
</body>
</html>
```